Corvale Mechanical - Letterhead

We are a plumbing and hvac company based in Calgary. This letterhead will be on our quotes, invoices, preventative maintenance proposals etc.

```html
<!DOCTYPE html>
<html lang="en">
<head>
<meta charset="utf-8">
<title>Corvale Mechanical – Letterhead</title>
<link href="https://fonts.googleapis.com/css2?family=Open+Sans:wght@400;700&family=Roboto:wght@400&display=swap" rel="stylesheet">
<style>
  :root {
    --backdrop: #dedede;
    --paper: #fafafa;
    --brand-blue: #1f70b5;
    --brand-orange: #e95a28;
    --body-ink: #555555;
    --contact-ink: #3c3c3c;
    --signature-tone: #e6e6e6;
  }
  * { margin: 0; padding: 0; box-sizing: border-box; }
  html, body {
    width: 1200px; height: 800px; overflow: hidden;
    background: var(--backdrop);
  }
  .letterhead {
    position: absolute;
    left: 330px; top: 23px;
    width: 540px; height: 754px;
    background: var(--paper);
    font-family: "Open Sans", Arial, sans-serif;
    color: var(--body-ink);
  }
  .brand {
    position: absolute;
    left: 49px; top: 62px;
    display: flex; align-items: center; gap: 7px;
  }
  .brand-dot {
    width: 14px; height: 14px; border-radius: 50%;
    background: var(--brand-orange);
  }
  .brand-name {
    font-weight: 700; font-size: 13px;
    color: var(--brand-blue);
    letter-spacing: 0.2px;
  }
  .contact {
    position: absolute;
    left: 361px; top: 53px;
    border-left: 1.5px solid var(--brand-blue);
    padding-left: 14px;
    height: 63px;
    font-family: "Roboto", Arial, sans-serif;
    font-size: 9.4px; line-height: 12px;
    color: var(--contact-ink);
  }
  .contact .address { margin-bottom: 2px; }
  .contact-line { display: flex; align-items: center; gap: 3px; }
  .contact-line svg { width: 8px; height: 8px; flex: none; }
  .letter-body {
    position: absolute;
    left: 49px; top: 175px;
    width: 443px;
    font-size: 9.6px; line-height: 14.5px;
  }
  .letter-body p { text-align: justify; margin-bottom: 14.5px; }
  .letter-body .salutation, .letter-body .closing { text-align: left; }
  .signature {
    position: absolute;
    left: 49px; top: 555px;
    width: 62px; height: 60px;
    background: var(--signature-tone);
  }
  .footer-bands {
    position: absolute;
    left: 0; bottom: 0;
    width: 100%; height: 13px;
    display: flex; gap: 3px;
  }
  .footer-bands span { flex: 1; }
  .band-blue { background: var(--brand-blue); }
  .band-orange { background: var(--brand-orange); }
</style>
</head>
<body>
  <div class="letterhead">
    <div class="brand">
      <span class="brand-dot"></span>
      <span class="brand-name">Corvale Mechanical</span>
    </div>

    <div class="contact">
      <div class="address">2180 Harlow Street,<br>Suite 410 Calgary.</div>
      <div class="contact-line">
        <svg viewBox="0 0 10 10"><path d="M1 4c0-2 8-2 8 0v1H7V4H3v1H1z M2 6h6l1 3H1z" fill="var(--brand-orange)"/></svg>
        403.555.0148
      </div>
      <div class="contact-line">
        <svg viewBox="0 0 10 10"><rect x="0.5" y="2" width="9" height="6.5" fill="var(--brand-orange)"/><path d="M0.5 2L5 6l4.5-4" stroke="#fff" stroke-width="1" fill="none"/></svg>
        info@corvalemech.com
      </div>
      <div class="contact-line">
        <svg viewBox="0 0 10 10"><circle cx="5" cy="5" r="4.5" fill="var(--brand-orange)"/><path d="M3 3c1 1 2 0 2 2s-2 1-1 3M6 2c1 1 0 2 2 3" stroke="#fff" stroke-width="0.9" fill="none"/></svg>
        www.corvalemech.com
      </div>
    </div>

    <div class="letter-body">
      <p class="salutation">Dear customer,</p>
      <p>Lorem ipsum dolor sit amet, consectetur adipisicing elit, sed do eiusmod tempor incididunt ut labore et dolore magna aliqua. Ut enim ad minim veniam, quis nostrud exercitation ullamco laboris nisi ut aliquip ex ea commodo consequat. Duis aute irure dolor in reprehenderit in voluptate velit esse cillum dolore eu fugiat nulla pariatur. Excepteur sint occaecat cupidatat non proident, sunt in culpa qui officia deserunt mollit anim id est laborum.</p>
      <p>Lorem ipsum dolor sit amet, consectetur adipisicing elit, sed do eiusmod tempor incididunt ut labore et dolore magna aliqua. Ut enim ad minim veniam, quis nostrud exercitation ullamco laboris nisi ut aliquip ex ea commodo consequat. Duis aute irure dolor in reprehenderit in voluptate velit esse cillum dolore eu fugiat nulla pariatur. Excepteur sint occaecat cupidatat non proident, sunt in culpa qui officia deserunt mollit anim id est laborum.</p>
      <p>Lorem ipsum dolor sit amet, consectetur adipisicing elit, sed do eiusmod tempor incididunt ut labore et dolore magna aliqua. Ut enim ad minim veniam, quis nostrud exercitation ullamco laboris nisi ut aliquip ex ea commodo consequat. Duis aute irure dolor in reprehenderit in voluptate velit esse cillum dolore eu fugiat nulla pariatur. Excepteur sint occaecat cupidatat non proident, sunt in culpa qui officia deserunt mollit anim id est laborum.</p>
      <p>Lorem ipsum dolor sit amet, consectetur adipisicing elit, sed do eiusmod tempor incididunt ut labore et dolore magna aliqua. Ut enim ad minim veniam, quis nostrud exercitation ullamco laboris nisi ut aliquip ex ea commodo consequat. Duis aute irure dolor in reprehenderit.</p>
      <p class="closing">Yours Sincerely,</p>
    </div>

    <div class="signature" role="img" aria-label="Handwritten signature of the sender"></div>

    <div class="footer-bands">
      <span class="band-blue"></span>
      <span class="band-orange"></span>
      <span class="band-blue"></span>
    </div>
  </div>
</body>
</html>
```